依頼詳細
イベントチラシの為、お子様連れのファミリー層が来たくなるようワクワク感のあるテイストでお願いします。
記載項目
記載内容につきましては、aiデータにまとめましたので下記サイトより
ダウンロードにてご確認くださいませ。
aiデータに落とし込んでいる内容は原稿として捉えて頂きまして、フォント・レイアウト・イラスト・キャッチコピー等は自由に変更してください。
https://kumobako-share.jp/download/8c3a91d02e7b45f6a0c9d1e3b7f24a5c6e8d0b19
以上よろしくお願い申し上げます。
サイズ
B4
ページ数
両面
希望イメージ
シンプル 複雑
単色 カラフル
暗い 明るい
日常 高級
遊び心 厳粛
未来的 伝統的
女性的 男性的
希望する色
納品ファイル
• イラストレーター形式 (.ai)
補足説明
お世話になっております。
分譲地のロゴとQRコードのデータが埋め込まれていなかったみたいですので
追加に送付させていただきます。
お手数をおかけしますが、ご確認よろしくお願い致します。
お世話になっております。
素晴らしい作品をご提案頂きまして、誠にありがとうございました。
検討させていただきますので、しばらくお待ちくださいませ。

よろしくお願いいたします。
■ 選んだ理由

真夏のイベントですが、清涼感があり、全体的なレイアウトも非常に分かり易くまとめて頂いた所が、高く評価されました。

■ 提案者全員のお礼・コメント

多くの皆様にご参加頂きまして、誠にありがとうございました。
素晴らしい作品が沢山ありましたので、次回制作ではコンペではなく
プロジェクトで申請させて頂くかもしれませんので、その際には
何卒よろしくお願い申し上げます。

```html
<!DOCTYPE html>
<html lang="ja">
<head>
<meta charset="utf-8">
<title>ひなた街 夏祭り</title>
<link rel="stylesheet" href="https://fonts.googleapis.com/css2?family=Dela+Gothic+One&family=M+PLUS+Rounded+1c:wght@500;800;900&display=swap">
<style>
:root{
  --sky:#d6eef8;
  --navy:#1d3a7a;
  --red:#e2322b;
  --yellow:#ffd83a;
  --green:#3aa845;
  --orange:#f28a1c;
  --white:#ffffff;
  --ink:#2b2b2b;
  --foot:#4a4a4a;
}
*{box-sizing:border-box;margin:0;padding:0}
html,body{width:861px;height:1200px;overflow:hidden}
body{font-family:"M PLUS Rounded 1c",sans-serif;color:var(--ink);background:var(--white)}
.flyer{position:relative;width:861px;height:1200px;overflow:hidden;
  background:radial-gradient(circle,var(--white) 2px,transparent 3px) 0 0/28px 28px,linear-gradient(var(--sky),#eaf6fb)}
.abs{position:absolute}
.bunting{left:0;top:0;width:861px;height:70px;background:linear-gradient(90deg,#f6b7c8,#fde28a,#a9dcf3,#bfe5a8,#f6b7c8)}
.brand-box{left:30px;top:28px;width:100px;height:92px;background:var(--white);border-radius:6px;display:flex;flex-direction:column;align-items:center;justify-content:center;gap:6px;font-weight:800;color:var(--navy);font-size:14px}
.brand-box i{width:38px;height:38px;border-radius:50%;background:var(--navy)}
.brand-right{right:30px;top:36px;background:var(--white);padding:8px 14px;border-radius:6px;text-align:right}
.brand-right small{display:block;font-size:9px;color:var(--navy)}
.brand-right b{font-size:17px;color:var(--red);font-weight:800}
.times{left:172px;top:52px;font-size:11px;font-weight:800;color:var(--navy);background:var(--white);padding:3px 10px;border-radius:10px}
.date{left:0;width:861px;top:72px;text-align:center;font-family:"Dela Gothic One",sans-serif;color:var(--red);font-size:58px;line-height:1}
.date .dow{display:inline-block;background:var(--navy);color:var(--white);border-radius:50%;font-size:22px;width:36px;height:36px;line-height:36px;vertical-align:middle}
.date .day{font-size:40px}
.place{left:0;width:861px;top:138px;text-align:center;font-weight:900;font-size:34px;color:var(--navy)}
.title{left:0;width:861px;top:180px;text-align:center;font-family:"Dela Gothic One",sans-serif;font-size:150px;line-height:1;color:var(--red);
  text-shadow:5px 5px 0 var(--yellow),-3px -3px 0 var(--white),3px -3px 0 var(--white),-3px 3px 0 var(--white)}
.reserve{left:34px;top:200px;width:120px;height:120px;border-radius:50%;background:var(--green);color:var(--white);font-weight:900;font-size:24px;display:flex;align-items:center;justify-content:center;text-align:center;line-height:1.15}
.label{font-weight:900;color:var(--white);padding:4px 12px;border-radius:20px;font-size:20px;white-space:nowrap}
.art{border-radius:12px}
.badge-art{left:30px;top:395px;width:200px;height:120px;background:linear-gradient(#fbe3a0,#f6c86a)}
.badge-title{left:38px;top:355px;background:var(--orange)}
.badge-note{left:34px;top:520px;width:210px;font-size:11px;font-weight:800;color:var(--navy);line-height:1.4}
.kids-art{left:255px;top:345px;width:360px;height:230px;border-radius:24px;
  background:radial-gradient(circle at 30% 35%,#fbd6a6 0 22%,transparent 23%),
             radial-gradient(circle at 70% 45%,#f59a8a 0 20%,transparent 21%),
             radial-gradient(circle at 50% 70%,#8fc7ee 0 24%,transparent 25%),
             linear-gradient(135deg,#fff1c9,#fcd9b8 55%,#cfe8f6)}
.yoyo{left:640px;top:345px;background:var(--green)}
.yoyo-art{left:650px;top:330px;width:60px;height:60px;border-radius:50%;background:linear-gradient(#ff9fb8,#8fd1f1);opacity:.7}
.ice{left:640px;top:400px;width:190px;background:var(--white);border-radius:12px;padding:10px;font-weight:900;color:var(--navy);font-size:16px;line-height:1.3}
.ice em{font-style:normal;color:var(--red)}
.ice-art{margin-top:6px;height:56px;border-radius:8px;background:linear-gradient(90deg,#fbb3c4,#fde58e,#a8dcf4)}
.gun{left:650px;top:530px;background:var(--red);font-size:15px}
.row2{top:590px;height:260px;display:flex;flex-direction:column}
.card{background:var(--white);border-radius:14px;padding:10px}
.row2 h3{font-weight:900;font-size:22px;text-align:center;line-height:1.2;white-space:nowrap}
.row2 .art{margin-top:8px;flex:1;min-height:0}
.hotdog{left:24px;width:260px}
.hotdog h3{color:var(--red)}
.hotdog .art{background:linear-gradient(#cfd5db,#6f7880)}
.cars{left:298px;width:266px}
.cars h3{color:var(--navy)}
.cars .art{background:linear-gradient(#dfe8ef,#88949e)}
.beetle{left:578px;width:259px}
.beetle h3{color:#6b3d14}
.beetle h3 small{display:block;font-size:17px}
.beetle .art{background:linear-gradient(#e7d6b5,#7a5a2e)}
.row3{top:868px;height:200px}
.view{left:24px;width:430px;display:flex;gap:10px}
.view p{font-size:13px;font-weight:800;color:var(--navy);line-height:1.5;width:150px}
.view .art{flex:1;height:180px;background:linear-gradient(#bfe2f5,#8cbf7d)}
.floor{left:24px;top:1040px;font-size:12px;font-weight:800;background:var(--navy);color:var(--white);padding:3px 10px;border-radius:10px}
.bounce{left:470px;width:367px}
.bounce h3{font-weight:900;font-size:26px;color:var(--orange);text-align:center}
.bounce-body{display:flex;gap:8px;margin-top:6px}
.bounce-body p{font-size:12px;font-weight:800;color:var(--navy);line-height:1.5;width:140px;background:#fff6d6;padding:8px;border-radius:8px}
.bounce-body .art{flex:1;height:120px;background:linear-gradient(#f9a0b0,#e94c5d)}
.footer{left:0;top:1085px;width:861px;height:115px;background:var(--foot);color:var(--white);display:flex;align-items:center;padding:0 30px;gap:24px}
.footer .co{font-weight:900;font-size:28px;color:var(--white);display:flex;align-items:center;gap:10px}
.footer .co i{width:22px;height:22px;background:var(--white)}
.footer .co small{display:block;font-size:10px;font-weight:500}
.contact{margin-left:auto;text-align:right}
.contact .lead{font-size:13px;font-weight:800}
.contact .tel{font-family:"Dela Gothic One",sans-serif;font-size:34px;display:flex;align-items:center;gap:8px;justify-content:flex-end}
.mail{background:var(--white);color:var(--foot);font-weight:800;font-size:13px;padding:8px 12px;border-radius:8px}
</style>
</head>
<body>
<main class="flyer">
  <div class="abs bunting" role="img" aria-label="カラフルな三角旗のガーランド"></div>
  <div class="abs brand-box"><i></i>HINATA</div>
  <div class="abs times">各回2部制 ① 10:00〜13:00 ② 13:00〜16:00</div>
  <div class="abs brand-right"><small>暮らしを楽しむ家づくり</small><b>ミナモハウス</b></div>

  <div class="abs date">8/7<span class="dow">土</span>・8<span class="day">日</span></div>
  <div class="abs place">千草市ひなた街</div>
  <h1 class="abs title">夏祭り</h1>
  <div class="abs reserve">完全<br>予約制</div>

  <div class="abs label badge-title">缶バッジ作り</div>
  <div class="abs art badge-art" role="img" aria-label="手作りの缶バッジのイラスト"></div>
  <p class="abs badge-note">お子様の似顔絵や写真で、世界に一つだけの缶バッジを作ろう！</p>

  <div class="abs art kids-art" role="img" aria-label="太鼓を叩く浴衣姿の子どもたちと提灯のお祭りイラスト"></div>

  <div class="abs art yoyo-art" role="img" aria-label="水風船ヨーヨーのイラスト"></div>
  <div class="abs label yoyo">ヨーヨー釣り</div>
  <div class="abs ice">カップかき氷アイス<br><em>プレゼント！</em>
    <div class="ice-art" role="img" aria-label="カップかき氷アイスのイラスト"></div>
  </div>
  <div class="abs label gun">水鉄砲の的あて！</div>

  <section class="abs row2 card hotdog">
    <h3>ホットドッグも<br>販売するよ！</h3>
    <div class="art" role="img" aria-label="キッチンカーの写真"></div>
  </section>
  <section class="abs row2 card cars">
    <h3>はたらく<br>クルマ大集合！</h3>
    <div class="art" role="img" aria-label="パトカーや白バイなど働く車の写真"></div>
  </section>
  <section class="abs row2 card beetle">
    <h3>カブトムシ<small>ふれあい体験＆プレゼント！</small></h3>
    <div class="art" role="img" aria-label="カブトムシの写真"></div>
  </section>

  <section class="abs row3 card view">
    <p>2階以上から眺める特別な見学体験。屋根の上から夏祭りを見下ろそう！</p>
    <div class="art" role="img" aria-label="建物からの眺望写真"></div>
  </section>
  <div class="abs floor">4階建て住宅の見学もできます</div>
  <section class="abs row3 card bounce">
    <h3>ふわふわがやってくる！</h3>
    <div class="bounce-body">
      <p>「おっきなワンちゃんのふわふわ」がやってくるよ！みんなで遊ぼう！</p>
      <div class="art" role="img" aria-label="エア遊具ふわふわの写真"></div>
    </div>
  </section>

  <footer class="abs footer">
    <div class="co"><i></i><span>ミナモハウス北陸<small>住まいの相談窓口</small></span></div>
    <div class="contact">
      <div class="lead">まずはお気軽にご予約ください！</div>
      <div class="tel"><svg width="30" height="30" viewBox="0 0 24 24" aria-hidden="true"><path fill="#fff" d="M6.6 10.8a15.1 15.1 0 0 0 6.6 6.6l2.2-2.2a1 1 0 0 1 1-.25 11.4 11.4 0 0 0 3.6.57 1 1 0 0 1 1 1V20a1 1 0 0 1-1 1A17 17 0 0 1 3 4a1 1 0 0 1 1-1h3.5a1 1 0 0 1 1 1c0 1.25.2 2.45.57 3.6a1 1 0 0 1-.25 1z"/></svg>000-123-4567</div>
    </div>
    <div class="mail">メールお申し込み</div>
  </footer>
</main>
</body>
</html>
```